Australian Civil Construction, Quarry & Mining Services needs a business card

We need a business card designed for our Civil Construction, Quarry & Mining Services based in the country in Australia.
Our Company Brindle Earthworks provide innovate solutions for infrastructure, agricultural and mining (aggregate, sand, roadbase) industry.
We would like our business cards to be double sided
Front of card: black background or something that resembles our business colours. (it doesn't have to be black we are open to options)
- Company name - Brindle Earthworks
- Either our logo or some sort of icon/picture that resembles our business
- Website - https://brindleearthworks-example.com.au/
- We will have a number of different names, positions descriptions, phone numbers and emails on separate cards for each of our managers/directors

```html
<!DOCTYPE html>
<html lang="en">
<head>
<meta charset="utf-8">
<title>Brindle Earthworks – Business Card</title>
<link rel="stylesheet" href="https://fonts.googleapis.com/css2?family=Montserrat:wght@800&family=Mulish:ital,wght@0,400;1,300&family=Questrial&display=swap">
<style>
  :root {
    --stage: #1e1e1e;
    --card: #1a1718;
    --orange: #f47f20;
    --orange-deep: #b5532a;
    --white: #ffffff;
    --silver: #c9c9cc;
  }
  * { margin: 0; padding: 0; box-sizing: border-box; }
  html, body { width: 1200px; height: 481px; overflow: hidden; }
  body { background: var(--stage); position: relative; }

  .card {
    position: absolute;
    top: 102px;
    width: 463px;
    height: 278px;
    background: var(--card);
    overflow: hidden;
    box-shadow: 0 4px 10px rgba(0,0,0,.45);
  }
  .card--front { left: 110px; }
  .card--back { left: 628px; }
  .card__art { position: absolute; inset: 0; width: 100%; height: 100%; }

  .holder { position: absolute; left: 157px; top: 84px; }
  .holder__name {
    font-family: "Questrial", sans-serif;
    font-size: 20px;
    color: var(--orange);
    letter-spacing: .3px;
    line-height: 1;
  }
  .holder__role {
    font-family: "Mulish", sans-serif;
    font-size: 12px;
    color: var(--white);
    margin: 3px 0 0 10px;
  }

  .contact {
    position: absolute;
    font-family: "Mulish", sans-serif;
    font-style: italic;
    font-weight: 300;
    font-size: 12px;
    color: var(--white);
    display: flex;
    align-items: center;
    gap: 3px;
    white-space: nowrap;
  }
  .contact svg { width: 10px; height: 10px; flex: none; }
  .contact--phone { left: 197px; top: 138px; }
  .contact--mail { left: 209px; top: 156px; }
  .contact--web { left: 222px; top: 173px; }

  .brand-mini {
    position: absolute;
    left: 360px; top: 52px;
    display: flex; align-items: center; gap: 5px;
  }
  .brand-mini__dot { width: 12px; height: 12px; border-radius: 50%; background: var(--orange); }
  .brand-mini__name {
    font-family: "Montserrat", sans-serif;
    font-weight: 800;
    font-size: 9px;
    line-height: 1.15;
    color: var(--white);
  }

  .brand-ring {
    position: absolute;
    left: 62px; top: 78px;
    width: 96px; height: 96px;
    border-radius: 50%;
    border: 3px solid var(--silver);
  }
  .brand-name {
    position: absolute;
    left: 0; width: 220px; top: 188px;
    text-align: center;
    font-family: "Montserrat", sans-serif;
    font-weight: 800;
    font-size: 15px;
    line-height: 1.05;
    letter-spacing: .5px;
    color: var(--white);
  }
</style>
</head>
<body>

  <section class="card card--front" aria-label="Card front">
    <svg class="card__art" viewBox="0 0 463 278" aria-hidden="true">
      <defs>
        <linearGradient id="bandFront" x1="0" y1="0" x2="0" y2="1">
          <stop offset="0" stop-color="#f47f20"/>
          <stop offset=".62" stop-color="#f47f20"/>
          <stop offset="1" stop-color="#b5532a"/>
        </linearGradient>
      </defs>
      <polygon points="35,0 139,0 297,278 195,278" fill="url(#bandFront)"/>
      <path class="tab" d="M156 82 H350 V130 H160 Q154 130 153 124 L146 92 Q145 82 156 82 Z" fill="#1a1718"/>
      <path class="tab" d="M198 135 H463 V194 H225 Q216 194 211 186 L193 148 Q189 135 198 135 Z" fill="#1a1718"/>
    </svg>

    <div class="holder">
      <p class="holder__name">JOHN DOE</p>
      <p class="holder__role">Manager</p>
    </div>

    <p class="contact contact--phone">
      <svg viewBox="0 0 10 10"><circle cx="5" cy="5" r="5" fill="#fff"/><path d="M3.2 2.4l1 1-.5.7a4 4 0 0 0 2.2 2.2l.7-.5 1 1-.7.8C5.6 7.6 2.4 4.4 2.4 3.1z" fill="#1a1718"/></svg>
      111-222-333
    </p>
    <p class="contact contact--mail">
      <svg viewBox="0 0 10 10"><circle cx="5" cy="5" r="5" fill="#fff"/><rect x="2.4" y="3.2" width="5.2" height="3.6" fill="none" stroke="#1a1718" stroke-width=".8"/><path d="M2.4 3.2L5 5.3 7.6 3.2" fill="none" stroke="#1a1718" stroke-width=".8"/></svg>
      info@brindleearthworks-example.com
    </p>
    <p class="contact contact--web">
      <svg viewBox="0 0 10 10"><circle cx="5" cy="5" r="4.5" fill="none" stroke="#fff" stroke-width=".9"/><ellipse cx="5" cy="5" rx="2" ry="4.5" fill="none" stroke="#fff" stroke-width=".7"/><path d="M.5 5h9M1.3 3h7.4M1.3 7h7.4" stroke="#fff" stroke-width=".6"/></svg>
      brindleearthworks-example.com.au
    </p>

    <div class="brand-mini">
      <span class="brand-mini__dot"></span>
      <span class="brand-mini__name">BRINDLE<br>EARTHWORKS</span>
    </div>
  </section>

  <section class="card card--back" aria-label="Card back">
    <svg class="card__art" viewBox="0 0 463 278" aria-hidden="true">
      <defs>
        <linearGradient id="bandBack" x1="0" y1="1" x2="1" y2="0">
          <stop offset="0" stop-color="#f47f20"/>
          <stop offset=".55" stop-color="#f47f20"/>
          <stop offset="1" stop-color="#9e4a24"/>
        </linearGradient>
      </defs>
      <polygon points="342,0 443,0 283,278 182,278" fill="url(#bandBack)"/>
    </svg>

    <span class="brand-ring"></span>
    <p class="brand-name">BRINDLE<br>EARTHWORKS</p>
  </section>

</body>
</html>
```